Spring Exterior Painting Advertisement

Attached is the postcard that we used last year(file - brightquill_318939...vector....pdf.. The information contained will be the same except for it will be updated for use during the spring of 2023.

The second attachment (sept 2021mailer) is another design that we've used in the past.

```html
<!DOCTYPE html>
<html lang="en">
<head>
<meta charset="utf-8">
<title>Harbor Painting – Spring Exterior Postcard</title>
<link rel="stylesheet" href="https://fonts.googleapis.com/css2?family=Gilda+Display&display=swap">
<style>
  :root {
    --navy: #1f222d;
    --green: #2bb673;
    --green-dark: #1e9a5c;
    --white: #ffffff;
    --ink: #111111;
    --rule: #2e4a66;
    --sky: #3a8fd8;
    --lawn: #5fb52a;
    --page: #ffffff;
  }
  * { margin: 0; padding: 0; box-sizing: border-box; }
  html, body { width: 1200px; height: 1000px; overflow: hidden; background: var(--page); }
  body { position: relative; font-family: "Gilda Display", Georgia, serif; color: var(--white); }

  .postcard { position: absolute; left: 291px; width: 585px; height: 397px; box-shadow: 6px 10px 22px rgba(0,0,0,0.12); }
  .postcard--front { top: 61px; }
  .postcard--back { top: 518px; background: var(--white); }

  .panel { position: absolute; left: 0; top: 0; width: 293px; height: 100%; background: var(--navy); }

  .brand { position: absolute; left: 51px; top: 30px; font-size: 11px; line-height: 1.1; letter-spacing: 0.5px; text-transform: uppercase; width: 60px; }

  .headline-box { position: absolute; left: 28px; top: 81px; width: 305px; height: 152px; background: var(--green); z-index: 2; }
  .headline-fold { position: absolute; left: 293px; top: 233px; z-index: 2; }
  .headline { position: absolute; left: 23px; top: 19px; font-size: 35px; line-height: 38px; font-weight: 400; white-space: nowrap; }

  .call { position: absolute; left: 51px; top: 255px; font-size: 11.5px; line-height: 19px; }
  .call-phone { display: flex; align-items: center; gap: 8px; }
  .address { position: absolute; left: 51px; top: 314px; font-size: 10.5px; line-height: 18px; font-style: normal; }

  .photo { position: absolute; left: 293px; top: 0; width: 292px; height: 397px;
    background: linear-gradient(180deg, var(--sky) 0%, #7fb8e6 30%, #6f8a5a 48%, #7b9c4a 62%, var(--lawn) 78%, #4fa021 100%); }
  .web { position: absolute; left: 59px; top: 332px; display: flex; align-items: center; gap: 6px; font-size: 10.5px; }

  .quote-title { position: absolute; left: 33px; top: 30px; font-size: 34px; line-height: 37px; font-weight: 400; white-space: nowrap; }
  .quote-copy { position: absolute; left: 34px; top: 112px; width: 250px; font-size: 11.2px; line-height: 15.6px; white-space: nowrap; }
  .services { position: absolute; left: 34px; top: 234px; width: 240px; list-style: none; display: grid; grid-template-columns: 126px 114px; grid-auto-flow: column; grid-template-rows: repeat(6, 22.3px); font-size: 11.5px; }
  .services li { display: flex; align-items: center; gap: 6px; }
  .services li::before { content: ""; width: 11px; height: 11px; border-radius: 50%; background: var(--white); flex: none; }

  .stamp { position: absolute; left: 476px; top: 34px; width: 76px; height: 76px; border: 1.5px solid var(--rule); }
  .address-line { position: absolute; left: 348px; width: 204px; height: 1.5px; background: var(--rule); }
  .offer-title { position: absolute; left: 348px; top: 233px; font-size: 29px; line-height: 36px; color: var(--ink); font-weight: 400; white-space: nowrap; }
  .offer-copy { position: absolute; left: 348px; top: 319px; font-size: 11.2px; line-height: 15.5px; color: var(--ink); white-space: nowrap; }
</style>
</head>
<body>

<section class="postcard postcard--front">
  <div class="panel">
    <div class="brand">Harbor Painting</div>
    <div class="call">
      <p>Call before it’s too late</p>
      <p class="call-phone">
        <svg width="14" height="14" viewBox="0 0 24 24" aria-hidden="true"><path fill="#fff" d="M6.6 10.8a15.1 15.1 0 0 0 6.6 6.6l2.2-2.2a1 1 0 0 1 1-.25 11.4 11.4 0 0 0 3.6.57 1 1 0 0 1 1 1V20a1 1 0 0 1-1 1A17 17 0 0 1 3 4a1 1 0 0 1 1-1h3.5a1 1 0 0 1 1 1c0 1.25.2 2.450.57 3.57a1 1 0 0 1-.25 1z"/></svg>
        (555) 014-2298
      </p>
    </div>
    <address class="address">
      Harbor Painting<br>18 Mill Creek Rd. Unit B<br>Lakeview, WI 53999
    </address>
  </div>
  <div class="headline-box"><h1 class="headline">Exterior job?<br>Get it painted<br>now!</h1></div>
  <svg class="headline-fold" width="40" height="36" aria-hidden="true"><polygon points="0,0 40,0 0,36" fill="var(--green-dark)"/></svg>
  <div class="photo" role="img" aria-label="Photo of a two-storey suburban house with landscaped garden and green lawn under blue sky">
    <div class="web">
      <svg width="18" height="18" viewBox="0 0 24 24" aria-hidden="true"><g fill="none" stroke="#fff" stroke-width="1.8"><circle cx="12" cy="12" r="10"/><ellipse cx="12" cy="12" rx="4.5" ry="10"/><path d="M2 12h20M4 7h16M4 17h16"/></g></svg>
      www.harborpaintingwi.com
    </div>
  </div>
</section>

<section class="postcard postcard--back">
  <div class="panel">
    <h2 class="quote-title">Request A Free<br>Exterior Quote</h2>
    <p class="quote-copy">Harbor Painting’s team offers painting and<br>staining for your home’s exterior surfaces.<br>From cement board siding to cedar, our<br>teams get the job done right. Homeowner<br>satisfaction and price transparency<br>is at the heart of our small business<br>serving you for over 18 years!</p>
    <ul class="services">
      <li>Pressure wash</li><li>Brick</li><li>Carpentry</li><li>Shutters</li><li>Caulking</li><li>Pergolas</li>
      <li>Sanding</li><li>Decks</li><li>Siding</li><li>Sunrooms</li><li>Trim</li><li>Boathouses</li>
    </ul>
  </div>
  <div class="stamp"></div>
  <div class="address-line" style="top:152px"></div>
  <div class="address-line" style="top:185px"></div>
  <div class="address-line" style="top:219px"></div>
  <h3 class="offer-title">Spots still<br>left for spring!</h3>
  <p class="offer-copy">Get a quote and get it done<br>before summer! Mention the<br>coupon code SPRINGEXT23.</p>
</section>

</body>
</html>
```